Rebranded Food Company looking for a new Food Label design for our packaging

We have a new logo, now we are looking for a base label for our products.
This has to comply with Australian food standards legislation - Please looks at attached brief for clarity.
We have open minds and are willing to look outside of the norm so long as it is cost effective.
It can be a label or a sleeve or a totally new concept.
Updates

Low designer entries

Target Market(s)

85% - B2b & 15% B2C

Industry/Entity Type

Food

Font styles to use
Other font styles liked:
• Adelle / Museo

Colors

Designer to choose colors to be used in the design.

Requirements
Must have
• All the legal labelling requirements - set out in brief document
Nice to have
• Key is to see the food and not cover it all up

```html
<!DOCTYPE html>
<html lang="en">
<head>
<meta charset="utf-8">
<title>Napoli Sauce – Food Label</title>
<link rel="stylesheet" href="https://fonts.googleapis.com/css2?family=Zilla+Slab:wght@400;500;600;700&display=swap">
<style>
  :root {
    --label-red: #e62d4b;
    --label-red-deep: #c3143a;
    --band-grey: #f4f4f4;
    --panel-grey: #ededed;
    --ink: #2b2b2b;
    --brand-ink: #3b3b3b;
    --white: #ffffff;
    --page: #ffffff;
  }
  * { box-sizing: border-box; margin: 0; padding: 0; }
  html, body { width: 1200px; height: 718px; overflow: hidden; background: var(--page); }
  body { position: relative; font-family: "Zilla Slab", Georgia, serif; color: var(--ink); }

  .label {
    position: absolute; left: 50px; top: 53px;
    width: 1222px; height: 680px;
    transform: scale(0.9); transform-origin: 0 0;
  }
  .label-shape { position: absolute; inset: 0; }

  .use-by {
    position: absolute; left: 18px; top: 47px; width: 295px; height: 32px;
    background: var(--white); font-size: 19px; font-weight: 500;
    padding: 5px 12px; color: var(--ink);
  }
  .brand {
    position: absolute; left: 420px; top: 34px; height: 62px;
    display: flex; align-items: center; gap: 14px;
  }
  .brand-dot { width: 58px; height: 58px; border-radius: 50%; background: var(--label-red); }
  .brand-name { font-size: 58px; font-weight: 700; color: var(--brand-ink); letter-spacing: 1px; line-height: 1; }

  .product-name {
    position: absolute; left: 0; right: 0; top: 122px; text-align: center;
    font-size: 104px; font-weight: 700; color: var(--white); line-height: 1;
  }
  .pack-size {
    position: absolute; left: 0; right: 0; top: 252px; text-align: center;
    font-size: 54px; font-weight: 500; color: var(--white); line-height: 1;
  }

  .ingredients { position: absolute; left: 22px; top: 350px; width: 434px; color: var(--white); }
  .ingredients h2 { font-size: 24px; font-weight: 600; line-height: 1; margin-left: 2px; }
  .ingredients p { font-size: 15.4px; line-height: 17.1px; text-align: justify; margin-top: 5px; }

  .nutrition {
    position: absolute; left: 482px; top: 375px; width: 376px; height: 162px;
    background: var(--panel-grey); border-radius: 6px; padding: 6px 26px 0 20px;
    font-size: 13.5px; line-height: 16px;
  }
  .nutrition-head { display: flex; font-size: 11.5px; font-weight: 600; text-transform: uppercase; }
  .nutrition-head span:last-child { margin-left: auto; margin-right: 12px; }
  .nutrition-table { width: 100%; border-collapse: collapse; margin-top: 4px; }
  .nutrition-table th { font-size: 11.5px; font-weight: 500; color: var(--label-red); text-align: right; line-height: 13px; }
  .nutrition-table td { text-align: right; padding: 0; font-weight: 500; }
  .nutrition-table td:first-child { text-align: left; padding-left: 5px; }
  .nutrition-table .sub { padding-left: 8px !important; }
  .nutrition-table td:nth-child(2) { width: 80px; }
  .nutrition-table td:nth-child(3) { width: 80px; }
  .nutrition-note {
    position: absolute; left: 482px; top: 539px; width: 376px; text-align: center;
    font-size: 11.5px; font-weight: 600; color: var(--ink);
  }

  .info-block { position: absolute; left: 884px; color: var(--white); }
  .info-block h3 { font-size: 12.5px; font-weight: 700; text-transform: uppercase; }
  .allergens { top: 377px; }
  .heating { top: 471px; }
  .icon-row { display: flex; gap: 18px; margin-top: 12px; }
  .icon { width: 42px; text-align: center; font-size: 6px; font-weight: 700; text-transform: uppercase; }
  .icon svg { display: block; margin: 0 auto 3px; }
</style>
</head>
<body>
  <div class="label">
    <svg class="label-shape" width="1222" height="680" viewBox="0 0 1222 680" aria-hidden="true">
      <path d="M20 0 H1198 Q1220 0 1220 22 V100 L0 106 V22 Q0 0 20 0 Z" fill="var(--band-grey)"/>
      <path d="M2 104 Q320 110 620 128 Q940 136 1220 98 V540 Q1220 560 1196 566
               Q900 660 640 680 Q380 664 40 566 Q2 556 2 530 Z" fill="var(--label-red)"/>
    </svg>

    <div class="use-by">Use by date</div>

    <div class="brand">
      <span class="brand-dot"></span>
      <span class="brand-name">KETTLEWAY</span>
    </div>

    <h1 class="product-name">Napoli Sauce</h1>
    <p class="pack-size">Individual Pack - 12 Serves</p>

    <section class="ingredients">
      <h2>INGREDIENTS</h2>
      <p>Lorem ipsum dolor sit amet, consectetuer adipiscing elit, sed diam nonummy nibh euismod tincidunt ut laoreet dolore magna aliquam erat volutpat. Ut wisi enim ad minim veniam, quis nostrud exerci tation ullamcorper suscipit lobortis nisl ut aliquip ex ea commodo consequat. Duis autem vel eum iriure dolor in hendrerit in vulputate velit esse molestie consequat, vel illum dolore eu feugiat nulla facilisis at vero eros et accumsan et iusto odio dignissim qui blandit praesent luptatum zzril delenit augue duis dolore te</p>
    </section>

    <section class="nutrition">
      <div class="nutrition-head"><span>Servings per package: 0</span><span>Serving size: 100g</span></div>
      <table class="nutrition-table">
        <tr><th></th><th>Per serving</th><th>Per 100g</th></tr>
        <tr><td>Energy</td><td>1263Kj</td><td>1263Kj</td></tr>
        <tr><td>Protein</td><td>13g</td><td>13g</td></tr>
        <tr><td>Fat, total</td><td>14.8g</td><td>14.8g</td></tr>
        <tr><td class="sub">-Saturated</td><td>6.3g</td><td>6.3g</td></tr>
        <tr><td>Carbohydrate</td><td>28.5g</td><td>28.5g</td></tr>
        <tr><td class="sub">-Sugars</td><td>4.9g</td><td>4.9g</td></tr>
        <tr><td>Sodium</td><td>756mg</td><td>756mg</td></tr>
      </table>
    </section>
    <p class="nutrition-note">All values are considered averages unless otherwise indicated</p>

    <section class="info-block allergens">
      <h3>Allergen information</h3>
      <div class="icon-row">
        <div class="icon">
          <svg width="20" height="28" viewBox="0 0 20 28" fill="var(--white)">
            <rect x="9" y="4" width="2" height="24"/>
            <ellipse cx="10" cy="4" rx="2.5" ry="4"/>
            <ellipse cx="6" cy="10" rx="2.5" ry="4" transform="rotate(-35 6 10)"/>
            <ellipse cx="14" cy="10" rx="2.5" ry="4" transform="rotate(35 14 10)"/>
            <ellipse cx="6" cy="17" rx="2.5" ry="4" transform="rotate(-35 6 17)"/>
            <ellipse cx="14" cy="17" rx="2.5" ry="4" transform="rotate(35 14 17)"/>
          </svg>Gluten</div>
        <div class="icon">
          <svg width="24" height="28" viewBox="0 0 24 28" fill="none" stroke="var(--white)" stroke-width="2">
            <circle cx="6" cy="8" r="4"/><circle cx="12" cy="15" r="4"/><circle cx="18" cy="22" r="4"/>
          </svg>Soy</div>
        <div class="icon">
          <svg width="14" height="28" viewBox="0 0 14 28" fill="var(--white)">
            <rect x="4" y="1" width="6" height="5" rx="1"/>
            <path d="M4 7 H10 L12 12 V26 Q12 27 11 27 H3 Q2 27 2 26 V12 Z"/>
          </svg>Lactose</div>
      </div>
    </section>

    <section class="info-block heating">
      <h3>Heating instructions</h3>
      <div class="icon-row">
        <div class="icon">
          <svg width="26" height="28" viewBox="0 0 26 28" fill="none" stroke="var(--white)" stroke-width="1.8">
            <path d="M3 16 H23 Q22 26 13 26 Q4 26 3 16 Z"/>
            <path d="M13 4 L18 8 L15 11 L10 7 Z" fill="var(--white)"/>
          </svg>1 Step</div>
        <div class="icon">
          <svg width="32" height="28" viewBox="0 0 32 28" fill="none" stroke="var(--white)" stroke-width="1.8">
            <rect x="2" y="5" width="28" height="18" rx="2"/>
            <rect x="6" y="9" width="15" height="10"/>
            <line x1="25" y1="9" x2="27" y2="9"/><line x1="25" y1="13" x2="27" y2="13"/><line x1="25" y1="17" x2="27" y2="17"/>
          </svg>2 Step</div>
        <div class="icon">
          <svg width="26" height="28" viewBox="0 0 26 28" fill="none" stroke="var(--white)" stroke-width="1.8">
            <circle cx="13" cy="15" r="9"/>
            <path d="M13 15 V10 M13 15 L17 17"/>
            <line x1="11" y1="4" x2="15" y2="4"/>
          </svg>3 Step</div>
      </div>
    </section>
  </div>
</body>
</html>
```